Marcus Delwyn-Hart Finance

Need a personal website advertising Equipment Finance,Business Finance,Commercial Finance, Construction Finance, Bridging Finance. Similar websites are www.qorvimark.com.au / www.talsbrio.com.au / www.zpk7.com.au /wwwlemberwick.com.au

Target Market(s)

Business People

Industry/Entity Type

Business

Number of Pages Required

3 page

Font styles to use
Serif
Sans Serif

Requirements
Must have
• All i want is a simple corporate looking website advertising Equipment Finance, Commercial Finance, Construction Finance, Business Finance, Bridging Finance,

```html
<!DOCTYPE html>
<html lang="en">
<head>
<meta charset="utf-8">
<title>Marcus Delwyn-Hart Finance</title>
<link rel="stylesheet" href="https://fonts.googleapis.com/css2?family=Barlow:wght@300;400;500;600;700&family=Open+Sans:wght@400;600;700&display=swap">
<style>
:root{
  --orange:#f15a2b;
  --orange-dark:#d9481c;
  --ink:#222222;
  --text:#555555;
  --muted:#888888;
  --line:#e4e4e4;
  --white:#ffffff;
  --footer:#2a2a2a;
  --hero-a:#3a3a3a;
  --hero-b:#141414;
}
*{box-sizing:border-box;margin:0;padding:0}
html,body{width:1200px;height:3482px;overflow:hidden}
body{font-family:"Open Sans",Arial,sans-serif;color:var(--text);background:var(--white)}
.page{position:relative;width:1200px;height:3482px;overflow:hidden}
.abs{position:absolute}
h1,h2,h3,h4,.display{font-family:"Barlow",Arial,sans-serif}

/* header & hero */
.hero{left:0;top:0;width:1200px;height:640px;background:radial-gradient(ellipse at 60% 40%,var(--hero-a),var(--hero-b))}
.brand{left:155px;top:20px;color:var(--white);font-family:"Barlow",sans-serif;font-weight:500;font-size:17px;letter-spacing:.3px}
.nav{right:155px;top:20px;display:flex;gap:30px;font-size:13px;color:var(--white)}
.nav span.caret::after{content:" \25BE";font-size:10px}
.topline{left:155px;top:62px;width:890px;height:1px;background:rgba(255,255,255,.15)}
.social{left:155px;top:91px;display:flex;gap:18px}
.social i{display:block;width:10px;height:10px;border-radius:50%;background:var(--white)}
.social i.hot{background:var(--orange)}
.phone{left:858px;top:78px;width:182px;height:40px;border-radius:20px;background:var(--orange);color:var(--white);font-size:14px;display:flex;align-items:center;justify-content:center;gap:8px}
.hero-title{left:0;top:244px;width:1200px;text-align:center;color:var(--white);font-weight:300;font-size:31px}
.hero-title b{font-weight:500}
.hero-sub{left:350px;top:293px;width:500px;text-align:center;color:#ddd;font-size:12.5px;line-height:19px}
.hero-btn{left:519px;top:356px;width:164px;height:38px;border:1px solid var(--white);border-radius:19px;color:var(--white);font-size:12px;display:flex;align-items:center;justify-content:center}
.dots{left:573px;top:531px;display:flex;gap:12px}
.dots i{width:10px;height:10px;border-radius:50%;border:2px solid var(--white)}
.dots i.on{background:var(--orange);border-color:var(--orange)}

/* service cards */
.card{top:640px;width:205px;height:290px;background:var(--white);box-shadow:0 2px 12px rgba(0,0,0,.1);text-align:center}
.card.featured{top:598px;height:350px;background:var(--orange);box-shadow:none}
.card-icon{position:absolute;left:50%;top:-48px;margin-left:-51px;width:102px;height:102px;border-radius:50%;background:var(--white);box-shadow:0 2px 10px rgba(0,0,0,.12);display:flex;align-items:center;justify-content:center}
.card.featured .card-icon{top:-4px;background:#2b2b2b;border:4px solid var(--orange);box-shadow:none}
.card h3{position:absolute;left:16px;right:16px;top:74px;font-size:14px;font-weight:600;color:var(--ink);line-height:18px}
.card.featured h3{top:116px;color:var(--white)}
.card p{position:absolute;left:22px;right:22px;top:122px;font-size:11.5px;line-height:18px;color:var(--muted)}
.card.featured p{top:164px;color:var(--white)}
.card .more{position:absolute;left:50%;margin-left:-72px;top:206px;width:144px;height:36px;border-radius:18px;border:1px solid var(--orange);font-size:11px;color:var(--ink);display:flex;align-items:center;justify-content:center}
.card.featured .more{top:252px;background:var(--white);border-color:var(--white)}

/* services that work */
.sec-title{left:0;top:1034px;width:1200px;text-align:center;font-size:24px;font-weight:400;color:var(--ink)}
.sec-sub{left:330px;top:1069px;width:540px;text-align:center;font-size:11px;line-height:15px;color:var(--muted)}
.offer{width:280px;text-align:center;padding-bottom:12px;border-bottom:1px solid var(--line)}
.offer svg{display:block;margin:0 auto 6px}
.offer h4{font-size:13px;font-weight:600;color:var(--ink);margin-bottom:6px}
.offer.active h4{color:var(--orange)}
.offer p{font-size:11px;line-height:15px;color:var(--muted)}
.people{left:452px;top:1172px;width:292px;height:385px;background:linear-gradient(180deg,#f2ece6,#d8d0c8 60%,#bdb3a9);border-radius:4px}

/* help band */
.help{left:0;top:1560px;width:1200px;height:558px;background:linear-gradient(90deg,#f4f4f4,#fbfbfb 50%,#eeeeee)}
.help-kicker{left:155px;top:1746px;font-size:15px;color:var(--ink)}
.help-title{left:155px;top:1768px;font-size:31px;font-weight:600;color:var(--ink)}
.help-title em{font-style:normal;color:var(--orange)}
.help-text{left:155px;top:1823px;width:460px;font-size:12px;line-height:20px;color:var(--muted)}
.help-btn{left:155px;top:1899px;width:166px;height:36px;border:1.5px solid var(--ink);border-radius:18px;font-size:12px;color:var(--ink);display:flex;align-items:center;justify-content:center}

/* blog */
.post{top:2200px;width:279px;height:411px;background:var(--white);box-shadow:0 2px 12px rgba(0,0,0,.1)}
.post-img{position:absolute;left:0;top:0;width:279px;height:164px}
.post-date{position:absolute;left:22px;top:132px;width:62px;height:70px;background:var(--white);border:2px solid var(--orange);text-align:center;font-family:"Barlow",sans-serif}
.post-date b{display:block;font-size:26px;font-weight:600;color:var(--ink);line-height:38px}
.post-date span{display:block;font-size:11px;background:var(--white);color:var(--muted);border-top:1px solid var(--line);line-height:22px;text-transform:uppercase}
.post h3{position:absolute;left:22px;right:22px;top:222px;font-size:14px;font-weight:600;color:var(--ink);line-height:18px}
.post p{position:absolute;left:22px;right:22px;top:272px;font-size:11.5px;line-height:18px;color:var(--muted)}
.post .rule{position:absolute;left:22px;top:374px;width:148px;height:2px;background:var(--orange)}
.post .read{position:absolute;right:26px;top:366px;font-size:11px;color:var(--ink)}

/* testimonial */
.testi{left:0;top:2688px;width:1200px;height:400px;background:linear-gradient(90deg,#eeeeee,#f7f7f7 50%,#ebebeb)}
.thumbs{left:320px;top:2756px;display:flex;align-items:center;gap:6px}
.thumbs i{display:block;width:68px;height:78px;background:linear-gradient(180deg,#c8c8c8,#8e8e8e)}
.thumbs i.sel{width:106px;height:106px;border:3px solid var(--white);background:linear-gradient(180deg,#d8c8bc,#9c8a80);margin:0 6px}
.testi-line{left:232px;top:2878px;width:736px;height:1px;background:#cfcfcf}
.testi-mark{left:554px;top:2876px;width:92px;height:3px;background:var(--orange)}
.testi-text{left:250px;top:2904px;width:700px;text-align:center;font-size:12px;line-height:19px;color:var(--ink)}
.testi-quote{left:0;top:2975px;width:1200px;text-align:center;font-family:"Barlow",sans-serif;font-size:34px;font-weight:700;color:var(--ink)}
.testi-name{left:0;top:3014px;width:1200px;text-align:center;font-size:12px;font-weight:700;color:var(--ink)}

/* cta */
.cta{left:0;top:3088px;width:1200px;height:162px;background:var(--orange)}
.cta-title{left:0;top:3108px;width:1200px;text-align:center;color:var(--white);font-size:23px;font-weight:600;letter-spacing:1px}
.cta-sub{left:0;top:3142px;width:1200px;text-align:center;color:var(--white);font-size:12px}
.cta-btn{top:3178px;width:204px;height:38px;border-radius:19px;font-size:13px;display:flex;align-items:center;justify-content:center}
.cta-btn.ghost{left:383px;border:1.5px solid var(--white);color:var(--white)}
.cta-btn.solid{left:613px;background:var(--white);color:var(--ink)}

/* footer */
.footer{left:0;top:3250px;width:1200px;height:232px;background:var(--footer)}
.foot-name{left:155px;top:3302px;color:var(--white);font-family:"Barlow",sans-serif;font-size:18px;font-weight:600;letter-spacing:2px;text-transform:uppercase}
.foot-links{left:155px;width:340px;font-size:11.5px;color:#dddddd;line-height:19px}
.foot-links .on{color:var(--orange)}
.foot-copy{left:155px;top:3410px;font-size:11.5px;color:#bbbbbb}
.foot-social{left:840px;top:3306px;display:flex;gap:10px}
.foot-social i{display:block;width:32px;height:32px;border-radius:50%;border:1px solid #777}
.foot-social i.top{background:var(--orange);border-color:var(--orange);display:flex;align-items:center;justify-content:center}
.signup{left:664px;top:3365px;width:380px;height:36px;border-radius:18px;background:var(--white);overflow:hidden}
.signup span{position:absolute;left:20px;top:10px;font-size:11.5px;font-style:italic;color:var(--muted)}
.signup b{position:absolute;right:0;top:0;width:128px;height:36px;background:var(--orange);color:var(--white);font-size:11px;font-weight:600;letter-spacing:1px;display:flex;align-items:center;justify-content:center}
.foot-note{left:664px;top:3413px;width:380px;text-align:right;font-size:11.5px;color:#dddddd}
</style>
</head>
<body>
<div class="page">

  <!-- Header / hero -->
  <div class="abs hero" role="img" aria-label="Dark overhead photo of business people meeting around a table with laptops and documents"></div>
  <div class="abs brand">Marcus Delwyn-Hart Finance</div>
  <nav class="abs nav"><span>Home</span><span>About us</span><span class="caret">Services</span><span>Our team</span><span>Our blogs</span><span>Contact us</span></nav>
  <div class="abs topline"></div>
  <div class="abs social"><i></i><i class="hot"></i><i></i><i></i></div>
  <div class="abs phone">
    <svg width="14" height="14" viewBox="0 0 24 24"><path fill="#fff" d="M6.6 10.8a15 15 0 006.6 6.6l2.2-2.2c.3-.3.7-.4 1-.2 1.1.4 2.3.6 3.6.6.6 0 1 .4 1 1V20c0 .6-.4 1-1 1A17 17 0 013 4c0-.6.4-1 1-1h3.5c.6 0 1 .4 1 1 0 1.3.2 2.5.6 3.6.1.3 0 .7-.2 1z"/></svg>
    1-800-555-0147
  </div>
  <h1 class="abs hero-title display"><b>Finance</b> and lending professionals investors</h1>
  <p class="abs hero-sub">Lorem ipsum dolor sit amet, consectetur adipiscing elit, sed do eiusmod tempor incididunt ut labore et dolore magna</p>
  <div class="abs hero-btn">Contact us now &rsaquo;</div>
  <div class="abs dots"><i></i><i class="on"></i><i></i></div>

  <!-- Service cards -->
  <div class="abs card" style="left:155px">
    <div class="card-icon"><svg width="34" height="34" viewBox="0 0 34 34"><rect x="9" y="4" width="16" height="27" fill="#555"/><g fill="#fff"><rect x="12" y="8" width="3" height="3"/><rect x="19" y="8" width="3" height="3"/><rect x="12" y="14" width="3" height="3"/><rect x="19" y="14" width="3" height="3"/><rect x="12" y="20" width="3" height="3"/><rect x="19" y="20" width="3" height="3"/><rect x="15" y="25" width="4" height="6"/></g></svg></div>
    <h3>Business &amp; Commercial Lending</h3>
    <p>Nullam quis ante. Etiam sit amet orci eget eros faucibus tincidunt. Duis leo. Sed frin-gilla mauris sit amet.</p>
    <div class="more">Read More &rsaquo;</div>
  </div>
  <div class="abs card" style="left:385px">
    <div class="card-icon"><svg width="36" height="34" viewBox="0 0 36 34"><path d="M18 3L2 17h5v14h8v-9h6v9h8V17h5z" fill="#555"/></svg></div>
    <h3>Home Loans &amp; Investment Loans</h3>
    <p>Nullam quis ante. Etiam sit amet orci eget eros faucibus tincidunt. Duis leo. Sed frin-gilla mauris sit amet.</p>
    <div class="more">Read More &rsaquo;</div>
  </div>
  <div class="abs card featured" style="left:610px">
    <div class="card-icon"><svg width="40" height="30" viewBox="0 0 40 30"><path d="M8 12l4-8h16l4 8h3v10h-4v4h-5v-4H16v4h-5v-4H7V12z" fill="#fff"/><rect x="14" y="7" width="12" height="5" fill="#2b2b2b"/><circle cx="12" cy="17" r="2" fill="#2b2b2b"/><circle cx="28" cy="17" r="2" fill="#2b2b2b"/></svg></div>
    <h3>Motor Vehicle &amp; Equipment Finance</h3>
    <p>Nullam quis ante. Etiam sit amet orci eget eros faucibus tincidunt. Duis leo. Sed frin-gilla mauris sit amet.</p>
    <div class="more">Read More &rsaquo;</div>
  </div>
  <div class="abs card" style="left:840px">
    <div class="card-icon"><svg width="30" height="34" viewBox="0 0 30 34"><rect x="3" y="2" width="24" height="30" rx="2" fill="#555"/><rect x="7" y="6" width="16" height="6" fill="#fff"/><g fill="#fff"><rect x="7" y="15" width="4" height="3"/><rect x="13" y="15" width="4" height="3"/><rect x="19" y="15" width="4" height="3"/><rect x="7" y="21" width="4" height="3"/><rect x="13" y="21" width="4" height="3"/><rect x="19" y="21" width="4" height="9"/><rect x="7" y="27" width="10" height="3"/></g></svg></div>
    <h3>Consultancy Services</h3>
    <p>Nullam quis ante. Etiam sit amet orci eget eros faucibus tincidunt. Duis leo. Sed frin-gilla mauris sit amet.</p>
    <div class="more">Read More &rsaquo;</div>
  </div>

  <!-- Services that work -->
  <h2 class="abs sec-title">We Offer Services That Work</h2>
  <p class="abs sec-sub">The wise man therefore always holds in these matters to this principle of selection:<br>he rejects pleasures to secure other greater pleasures, or else he endures pains to avoid worse pains.</p>

  <div class="abs offer" style="left:155px;top:1130px">
    <svg width="28" height="24" viewBox="0 0 28 24"><g fill="none" stroke="#f15a2b" stroke-width="2"><path d="M2 22h24"/><rect x="5" y="12" width="4" height="10"/><rect x="12" y="6" width="4" height="16"/><rect x="19" y="2" width="4" height="20"/></g></svg>
    <h4>Equipment Finance</h4>
    <p>But I must explain to you how all this<br>idea of denouncing pleasure.</p>
  </div>
  <div class="abs offer active" style="left:155px;top:1256px">
    <svg width="28" height="24" viewBox="0 0 28 24"><g fill="none" stroke="#f15a2b" stroke-width="2"><circle cx="12" cy="8" r="5"/><path d="M3 22c1-6 17-6 18 0"/><path d="M21 4h5M23.5 1.5v5"/></g></svg>
    <h4>Business Finance</h4>
    <p>will give you a complete account of the<br>system, and expound the actual</p>
  </div>
  <div class="abs offer" style="left:155px;top:1386px">
    <svg width="28" height="24" viewBox="0 0 28 24"><g fill="none" stroke="#f15a2b" stroke-width="2"><rect x="3" y="5" width="22" height="14" rx="2"/><circle cx="14" cy="12" r="3"/></g></svg>
    <h4>Commercial Finance</h4>
    <p>The master-builder of human.<br>Rejects, dislikes, or avoids pleasure.</p>
  </div>

  <div class="abs people" role="img" aria-label="Photo of two business colleagues reviewing a folder together"></div>

  <div class="abs offer" style="left:766px;top:1130px">
    <svg width="28" height="24" viewBox="0 0 28 24"><g fill="none" stroke="#f15a2b" stroke-width="2"><path d="M2 22h24"/><rect x="5" y="8" width="6" height="14"/><rect x="14" y="3" width="8" height="19"/></g></svg>
    <h4>Construction Finance</h4>
    <p>But I must explain to you how all this<br>idea of denouncing pleasure.</p>
  </div>
  <div class="abs offer" style="left:766px;top:1256px">
    <svg width="28" height="24" viewBox="0 0 28 24"><g fill="none" stroke="#f15a2b" stroke-width="2"><path d="M2 16h24M5 16V9M23 16V9M5 9q9-7 18 0M11 16v-5M17 16v-5"/></g></svg>
    <h4>Bridging Finance</h4>
    <p>will give you a complete account of the<br>system, and expound the actual</p>
  </div>
  <div class="abs offer" style="left:766px;top:1386px">
    <svg width="28" height="24" viewBox="0 0 28 24"><g fill="none" stroke="#f15a2b" stroke-width="2"><rect x="3" y="5" width="22" height="14" rx="2"/><path d="M7 10h8M7 14h5"/></g></svg>
    <h4>Tax Planning</h4>
    <p>The master-builder of human.<br>Rejects, dislikes, or avoids pleasure.</p>
  </div>

  <!-- Help band -->
  <div class="abs help" role="img" aria-label="Faint, washed-out photo of a bright open-plan office"></div>
  <p class="abs help-kicker">Poor credit history or been told “no” by other lenders?</p>
  <h2 class="abs help-title">We’re here to <em>help</em> you.</h2>
  <p class="abs help-text">Lorem ipsum dolor sit amet, consectetur adipiscing elit. Ut elit tellus, luctus nec ullamcorper mattis, pulvinar dapibus leo. Amet consecte-tur adipiscing elit. Ut elit tellus, luctus nec ullamcorper mattis.</p>
  <div class="abs help-btn">Consult now &rsaquo;</div>
  <svg class="abs" style="left:612px;top:1624px" width="434" height="434" viewBox="0 0 434 434">
    <path d="M213 213V3A210 210 0 0 0 3 213Z" fill="#f15a2b"/>
    <path d="M221 213V3A210 210 0 0 1 431 213Z" fill="#9a9490" role="img" aria-label="Photo of a team meeting around a table"/>
    <path d="M213 221H3A210 210 0 0 0 213 431Z" fill="#c9c4c0" role="img" aria-label="Photo of a woman working at a laptop"/>
    <path d="M221 221H431A210 210 0 0 1 221 431Z" fill="#f15a2b"/>
    <g fill="none" stroke="#fff" stroke-width="3" stroke-linecap="round">
      <path d="M112 150a22 22 0 1 1 22 0v10h-22z"/><path d="M114 168h18"/>
      <path d="M84 124h-10M172 124h-10M123 84V74M96 97l-7-7M150 97l7-7"/>
    </g>
    <g fill="none" stroke="#fff" stroke-width="3">
      <circle cx="300" cy="280" r="8"/><path d="M288 322v-22q12-10 24 0v22"/>
      <circle cx="274" cy="290" r="6"/><path d="M264 322v-16q10-8 20 0"/>
      <circle cx="326" cy="290" r="6"/><path d="M316 306q10-8 20 0v16"/>
    </g>
  </svg>

  <!-- Blog -->
  <article class="abs post" style="left:155px">
    <div class="post-img" role="img" aria-label="Photo of people waiting seated in a modern office" style="background:linear-gradient(135deg,#c9c2b8,#7d766e)"></div>
    <div class="post-date"><b style="color:var(--orange)">18</b><span>Jun</span></div>
    <h3>Aenean accumsan ligula enea diam</h3>
    <p>Pellentesque nec tellus mauris. Fusce nec velit tincidunt tortor placerat semper. Nullam ultrices nunc ac dolor ultrices,...</p>
    <div class="rule"></div><div class="read">Read more &rsaquo;</div>
  </article>
  <article class="abs post" style="left:460px">
    <div class="post-img" role="img" aria-label="Photo of two businessmen in suits talking" style="background:linear-gradient(135deg,#d6d0c8,#5d5852)"></div>
    <div class="post-date"><b>09</b><span>Aug</span></div>
    <h3>Aenean accumsan ligula enea diam</h3>
    <p>Pellentesque nec tellus mauris. Fusce nec velit tincidunt tortor placerat semper. Nullam ultrices nunc ac dolor ultrices,...</p>
    <div class="rule"></div><div class="read">Read more &rsaquo;</div>
  </article>
  <article class="abs post" style="left:764px">
    <div class="post-img" role="img" aria-label="Photo of a busy open office with colleagues at desks" style="background:linear-gradient(135deg,#bdbdbd,#6c6c6c)"></div>
    <div class="post-date"><b>21</b><span>Sep</span></div>
    <h3>Aenean accumsan ligula enea diam</h3>
    <p>Pellentesque nec tellus mauris. Fusce nec velit tincidunt tortor placerat semper. Nullam ultrices nunc ac dolor ultrices,...</p>
    <div class="rule"></div><div class="read">Read more &rsaquo;</div>
  </article>

  <!-- Testimonials -->
  <div class="abs testi" role="img" aria-label="Faint photo of business people in a meeting"></div>
  <div class="abs thumbs" role="img" aria-label="Row of client portrait photos">
    <i></i><i></i><i class="sel"></i><i></i><i></i><i></i><i></i><i></i>
  </div>
  <div class="abs testi-line"></div>
  <div class="abs testi-mark"></div>
  <svg class="abs" style="left:130px;top:2866px" width="28" height="50" viewBox="0 0 28 50"><path d="M24 2L4 25l20 23" fill="none" stroke="#222" stroke-width="2"/></svg>
  <svg class="abs" style="left:1042px;top:2866px" width="28" height="50" viewBox="0 0 28 50"><path d="M4 2l20 23L4 48" fill="none" stroke="#f15a2b" stroke-width="2"/></svg>
  <p class="abs testi-text">Lorem ipsum dolor sit amet, consectetur adipiscing elit. Morbi hendrerit elit turpis, a porttitor tellus sollicitudin at.Class aptent taciti sociosqu ad litora torquent per conubia nostra, per inceptos himenaeos reprehenderit in voluptate velit esse cillum dolore eu fugiat</p>
  <div class="abs testi-quote">&ldquo;</div>
  <div class="abs testi-name">Maren Oakhurst - Brightline Media</div>

  <!-- CTA -->
  <div class="abs cta"></div>
  <h2 class="abs cta-title">GET YOUR FREE CONSULTING</h2>
  <p class="abs cta-sub">Our Expert Team Member</p>
  <div class="abs cta-btn ghost">Discover more &rsaquo;</div>
  <div class="abs cta-btn solid">Contact us &rsaquo;</div>

  <!-- Footer -->
  <footer class="abs footer"></footer>
  <div class="abs foot-name">Marcus Delwyn-Hart Finance</div>
  <div class="abs foot-links" style="top:3334px">Home &nbsp;|&nbsp; About us &nbsp;|&nbsp; <span class="on">Services</span> &nbsp;|&nbsp; Our team &nbsp;|&nbsp; Our blogs</div>
  <div class="abs foot-links" style="top:3353px">Contact Us &nbsp;|&nbsp; Terms &amp; Conditions &nbsp;|&nbsp; Privacy policy</div>
  <div class="abs foot-copy">&copy; 2017 Marcus Delwyn-Hart Finance. All rights reserved.</div>
  <div class="abs foot-social"><i></i><i></i><i></i><i></i><i></i>
    <i class="top"><svg width="12" height="12" viewBox="0 0 12 12"><path d="M6 1v10M1 6l5-5 5 5" fill="none" stroke="#fff" stroke-width="2"/></svg></i>
  </div>
  <div class="abs signup"><span>Enter your Email...</span><b>SUBSCRIBE</b></div>
  <div class="abs foot-note">Subscribe to our mailing list to get update to yor email.</div>
</div>
</body>
</html>
```